Business IT Services Billboard to attract local small businesses

We are Brivolux, a premier Managed Service Provider (MSP) specializing in comprehensive IT services and VOIP phone solutions exclusively for businesses. Our goal is to create a dynamic and visually engaging billboard advertisement that not only highlights our cutting-edge IT solutions but also emphasizes our state-of-the-art VOIP phone services. This billboard should communicate our commitment to providing innovative, reliable, and holistic technology solutions.
Target Market(s)
small business
Industry/Entity Type
Information Technology
Colors
Designer to choose colors to be used in the design.
Look and feel
Each slider illustrates characteristics of the customer's brand and the style your logo design should communicate.

```html
<!DOCTYPE html>
<html lang="en">
<head>
<meta charset="UTF-8">
<title>Brivolux – IT and VOIP Services Billboard</title>
<link rel="stylesheet" href="https://fonts.googleapis.com/css2?family=Krona+One&family=Poppins:wght@400;500;600;700&display=swap">
<style>
  :root {
    --page-bg: #c4c4c4;
    --navy: #0b2452;
    --sky: #2aa3f5;
    --white: #ffffff;
    --ink: #15192b;
    --photo-dark: #5d6a72;
    --photo-mid: #9aa6ad;
    --photo-light: #c9d2d6;
  }
  * { margin: 0; padding: 0; box-sizing: border-box; }
  html, body {
    width: 984px;
    height: 1200px;
    overflow: hidden;
    background: var(--page-bg);
  }
  .billboard {
    position: absolute;
    left: 42px;
    top: 406px;
    width: 900px;
    height: 388px;
    background: var(--white);
    box-shadow: 0 4px 14px rgba(0,0,0,0.25);
    overflow: hidden;
  }
  .billboard__shapes {
    position: absolute;
    inset: 0;
    width: 100%;
    height: 100%;
  }
  .headline-lead {
    position: absolute;
    left: 39px;
    top: 36px;
    font-family: "Poppins", sans-serif;
    font-weight: 400;
    font-size: 29px;
    letter-spacing: 5.2px;
    color: var(--white);
    white-space: nowrap;
  }
  .headline-main {
    position: absolute;
    left: 37px;
    top: 73px;
    font-family: "Krona One", sans-serif;
    font-size: 62px;
    line-height: 1;
    letter-spacing: -2px;
    color: var(--sky);
    white-space: nowrap;
  }
  .headline-sub {
    position: absolute;
    left: 39px;
    top: 143px;
    font-family: "Krona One", sans-serif;
    font-size: 29px;
    line-height: 1;
    letter-spacing: 0.4px;
    color: var(--white);
    white-space: nowrap;
  }
  .tagline {
    position: absolute;
    left: 37px;
    top: 185px;
    display: flex;
    align-items: center;
    gap: 8px;
  }
  .tagline__icon {
    width: 46px;
    height: 46px;
    border-radius: 50%;
    background: linear-gradient(135deg, #f5c23a, #e4474d 60%, #4f9be0);
  }
  .tagline__text {
    font-family: "Poppins", sans-serif;
    font-weight: 500;
    font-size: 23px;
    line-height: 25px;
    color: var(--white);
    white-space: nowrap;
  }
  .brand-name {
    position: absolute;
    left: 41px;
    top: 284px;
    font-family: "Poppins", sans-serif;
    font-weight: 700;
    font-size: 23px;
    color: var(--navy);
  }
  .cta {
    position: absolute;
    left: 154px;
    top: 257px;
    font-family: "Poppins", sans-serif;
    font-weight: 500;
    font-size: 25px;
    color: var(--ink);
    white-space: nowrap;
  }
  .url-pill {
    position: absolute;
    left: 157px;
    top: 300px;
    width: 415px;
    height: 38px;
    border: 1.5px solid var(--navy);
    border-radius: 0 20px 20px 0;
    background: var(--white);
    box-shadow: 0 9px 8px -6px rgba(0,0,0,0.45);
    display: flex;
    align-items: center;
    justify-content: center;
    font-family: "Poppins", sans-serif;
    font-weight: 500;
    font-size: 26px;
    letter-spacing: 2.6px;
    color: var(--ink);
  }
  .url-pill__domain {
    font-weight: 700;
    color: var(--navy);
  }
</style>
</head>
<body>
  <section class="billboard">
    <svg class="billboard__shapes" viewBox="0 0 1535 660" preserveAspectRatio="none">
      <defs>
        <linearGradient id="photoTone" x1="0" y1="0" x2="1" y2="1">
          <stop offset="0" stop-color="var(--photo-light)"/>
          <stop offset="0.5" stop-color="var(--photo-mid)"/>
          <stop offset="1" stop-color="var(--photo-dark)"/>
        </linearGradient>
      </defs>
      <polygon class="photo-area" points="1035,0 1535,0 1535,622 1078,622 943,302" fill="url(#photoTone)" role="img" aria-label="Photo of office colleagues reviewing work together at a laptop"/>
      <polygon class="navy-band" points="0,0 1035,0 943,304 0,304" fill="var(--navy)"/>
      <polygon class="sky-band" points="0,304 928,304 988,415 0,415" fill="var(--sky)"/>
    </svg>

    <p class="headline-lead">ELEVATE YOUR BUSINESS WITH</p>
    <h1 class="headline-main">NEXT-GEN</h1>
    <h2 class="headline-sub">IT AND VOIP SERVICES</h2>

    <div class="tagline">
      <div class="tagline__icon" role="img" aria-label="Team success icon"></div>
      <p class="tagline__text">Innovative IT and VOIP Solutions<br>Tailored for Your Business Success</p>
    </div>

    <p class="brand-name">Brivolux</p>
    <p class="cta">Transform Your Tech Today at</p>
    <p class="url-pill">www.<span class="url-pill__domain">brivolux</span>.com</p>
  </section>
</body>
</html>
```